Classy, Elegant, Simple Business Card Design

Looking to have a classy, simple, and elegant design. Want a top notch designed business card. I really like the look of the new brivo credit card. I also like the design I attached. I am trying to reach 21-29 year old females for booking us for there wedding or event. We offer Disc Jockey Service, Photo Booth Rentals, and Uplighting .

Target Market(s)

21-28 year old females

Contact Information for Business Card

Has to have logo, website, email, and phone number

Font styles to use
Other font styles liked:
• open to font choice, modern, clean
Designer to choose
33a6d7
0791cd
0555a3
ffffff

Requirements
Must have
• Has to have logo, website, email, and phone number
Nice to have
• I really like the design of the new brivo credit card. I also included my logo and some designs I like
Should not have
• clutter or too much info

```html
<!DOCTYPE html>
<html lang="en">
<head>
<meta charset="utf-8">
<title>Tidelight Event Group – Business Card</title>
<link href="https://fonts.googleapis.com/css2?family=Open+Sans:wght@400;600;700&display=swap" rel="stylesheet">
<style>
  :root {
    --brand-blue: #0093d9;
    --accent-strip: #5cbbe9;
    --navy: #1d3b66;
    --mid-blue: #0791cd;
    --ink: #111111;
    --white: #ffffff;
  }
  html, body {
    margin: 0;
    padding: 0;
    width: 1200px;
    height: 720px;
    overflow: hidden;
    background: var(--white);
    font-family: "Open Sans", Arial, sans-serif;
  }
  .card {
    position: relative;
    width: 1200px;
    height: 720px;
    background: var(--white);
  }
  .contact-panel {
    position: absolute;
    left: 3px;
    top: 0;
    width: 598px;
    height: 720px;
    background: var(--brand-blue);
    color: var(--white);
  }
  .accent-strip {
    position: absolute;
    left: 585px;
    top: 204px;
    width: 16px;
    height: 311px;
    background: var(--accent-strip);
  }
  .person-name {
    position: absolute;
    left: 89px;
    top: 142px;
    margin: 0;
    font-size: 42px;
    font-weight: 700;
    line-height: 1;
  }
  .person-title {
    position: absolute;
    left: 94px;
    top: 194px;
    margin: 0;
    font-size: 25px;
    font-weight: 400;
    line-height: 1;
  }
  .title-rule {
    position: absolute;
    left: 97px;
    top: 231px;
    width: 74px;
    height: 3px;
    background: var(--white);
  }
  .contact-list {
    position: absolute;
    left: 92px;
    top: 482px;
    margin: 0;
    padding: 0;
    list-style: none;
  }
  .contact-item {
    display: flex;
    align-items: center;
    height: 41px;
    font-size: 21px;
  }
  .contact-icon {
    width: 28px;
    height: 28px;
    margin-right: 24px;
    flex: none;
  }
  .brand-area {
    position: absolute;
    left: 601px;
    top: 0;
    width: 599px;
    height: 720px;
  }
  .brand-dot {
    position: absolute;
    left: 241px;
    top: 250px;
    width: 102px;
    height: 102px;
    border-radius: 50%;
    background: var(--mid-blue);
  }
  .brand-name {
    position: absolute;
    left: 0;
    top: 400px;
    width: 582px;
    margin: 0;
    text-align: center;
    font-size: 40px;
    font-weight: 600;
    letter-spacing: 1px;
    color: var(--navy);
  }
  .services {
    position: absolute;
    left: 0;
    top: 518px;
    width: 574px;
    margin: 0;
    text-align: center;
    font-size: 18px;
    color: var(--ink);
  }
</style>
</head>
<body>
<div class="card">
  <section class="contact-panel">
    <h1 class="person-name">Mara Ellison</h1>
    <p class="person-title">Founder &amp; CEO</p>
    <div class="title-rule"></div>
    <ul class="contact-list">
      <li class="contact-item">
        <svg class="contact-icon" viewBox="0 0 28 28" aria-hidden="true">
          <rect x="8" y="2" width="12" height="23" rx="2" fill="none" stroke="#fff" stroke-width="2"/>
          <circle cx="14" cy="21" r="1.3" fill="#fff"/>
        </svg>
        <span>123-456-789</span>
      </li>
      <li class="contact-item">
        <svg class="contact-icon" viewBox="0 0 28 28" aria-hidden="true">
          <path d="M3 10 C3 4 25 4 25 10 L20 11 L19 8 C16 7 12 7 9 8 L8 11 Z" fill="#fff"/>
          <path d="M7 13 L21 13 L24 24 L4 24 Z" fill="#fff"/>
          <circle cx="14" cy="18.5" r="3" fill="var(--brand-blue)"/>
        </svg>
        <span>123-456-789</span>
      </li>
      <li class="contact-item">
        <svg class="contact-icon" viewBox="0 0 28 28" aria-hidden="true">
          <rect x="2" y="6" width="24" height="17" fill="none" stroke="#fff" stroke-width="2"/>
          <path d="M2 6 L14 16 L26 6 M2 23 L11 14 M26 23 L17 14" fill="none" stroke="#fff" stroke-width="2"/>
        </svg>
        <span>info@yourwebsite.com</span>
      </li>
      <li class="contact-item">
        <svg class="contact-icon" viewBox="0 0 28 28" aria-hidden="true">
          <circle cx="14" cy="14" r="11" fill="none" stroke="#fff" stroke-width="2"/>
          <ellipse cx="14" cy="14" rx="5" ry="11" fill="none" stroke="#fff" stroke-width="2"/>
          <path d="M3 14 H25 M5 8 H23 M5 20 H23" stroke="#fff" stroke-width="2"/>
        </svg>
        <span>www.yourwebsite.com</span>
      </li>
    </ul>
    <div class="accent-strip"></div>
  </section>

  <section class="brand-area">
    <div class="brand-dot"></div>
    <p class="brand-name">Tidelight Event Group</p>
    <p class="services">Disc Jockey Service, Photo Booth Rentals, and Uplighting</p>
  </section>
</div>
</body>
</html>
```